Flyer-Design für 2-jährige Ausbildung in medizinischer Kosmetik gesucht
Tolle Designvorschläge, die gut die Vorgaben umgesetzt haben. Änderungswünsche und Fertigstellung erfolgten zügig und professionell. Unbedingt empfehlenswert.
Zielgruppe
2-jährige Vollzeitausbildung in Medizinische Kosmetik an einer Berufsfachschule in privater Trägerschaft (Schulgeld erforderlich, Förderung durch Bafög und der QZ möglich). Zielgruppe sind junge Frauen ab 16, die eine Ausbildung suchen.
Aufgabenstellung
Wir wünschen uns ein freches und modernes Design, das die 50-jährige Tradition der Privatschule und die klassische Schulausbildung aber trotzdem berücksichtigt.
Wünschenswert wäre die Einbindung eines zum Slogan passenden Bildes (Zeichnung oder Comics). Überwiegend in den Schulfarben gehalten (weiß, grün, grau/silber). Ein Plakat (DIN A 3) plus dazu passender Postkarte.

```html
<!DOCTYPE html>
<html lang="de">
<head>
<meta charset="utf-8">
<title>Havelstädter Fachschule für Hautpflege – Plakat und Postkarte</title>
<link rel="stylesheet" href="https://fonts.googleapis.com/css2?family=Open+Sans:wght@400;600;700&family=Kalam:wght@700&display=swap">
<style>
  :root {
    --green: #7ab51d;
    --green-dark: #67a012;
    --magenta: #d8137f;
    --grey-text: #555a5e;
    --white: #ffffff;
    --page: #eeeeec;
    --sans: "Open Sans", Arial, sans-serif;
    --hand: "Kalam", cursive;
  }
  * { box-sizing: border-box; margin: 0; padding: 0; }
  html, body { width: 736px; height: 1200px; overflow: hidden; }
  body { background: var(--page); font-family: var(--sans); position: relative; }

  .piece { position: absolute; background: var(--white); overflow: hidden; box-shadow: 0 2px 8px rgba(0,0,0,.12); }
  .poster { left: 148px; top: 24px; width: 440px; height: 620px; }
  .card { top: 706px; width: 330px; height: 470px; }
  .card--front { left: 22px; }
  .card--back { left: 384px; }

  .top-stripe { position: absolute; left: 0; top: 0; width: 100%; height: 14px; background: var(--green); }
  .header-rule { position: absolute; left: 0; width: 100%; height: 2px; background: var(--green); }

  .brand { position: absolute; display: flex; align-items: center; gap: 10px; }
  .brand__dot { border-radius: 50%; background: var(--green); flex: none; }
  .brand__name { color: var(--green); font-weight: 700; text-transform: uppercase; line-height: .98; letter-spacing: .2px; }

  .photo { position: absolute; }
  .photo--duo { background: linear-gradient(160deg, #f3eee6 0%, #e9d2bd 35%, #d9b596 55%, #efe6dc 80%, #f7f4ef 100%); }
  .photo--solo { background: radial-gradient(ellipse at 40% 45%, #dcb394 0%, #e8cdb6 40%, #f6efe8 75%, #ffffff 100%); }

  .slogan { position: absolute; font-family: var(--hand); font-weight: 700; color: var(--magenta); line-height: 1.05; transform: rotate(-7deg); transform-origin: left top; }
  .slogan--light { text-shadow: 0 0 6px rgba(255,255,255,.9); }

  .badge { position: absolute; border-radius: 50%; background: var(--magenta); border: 3px solid var(--white); color: var(--white); font-family: var(--hand); font-weight: 700; text-align: center; display: flex; align-items: center; justify-content: center; line-height: 1.05; }
  .badge span { transform: rotate(-14deg); display: block; }

  .info-phone { position: absolute; color: var(--magenta); font-weight: 700; }

  .band { position: absolute; left: 0; width: 100%; background: var(--green); color: var(--white); }
  .band__intro { font-weight: 600; text-transform: uppercase; }
  .band__intro strong { font-weight: 700; }
  .band__claim { font-weight: 700; text-transform: uppercase; }
  .band__web { font-weight: 400; }

  .back-copy { position: absolute; left: 0; width: 100%; text-align: center; color: var(--grey-text); font-size: 11px; line-height: 1.45; }
  .back-copy p + p { margin-top: 10px; }
  .back-copy .accent-pink { color: var(--magenta); }
  .back-copy .accent-green { color: var(--green); }
</style>
</head>
<body>

<section class="piece poster">
  <div class="top-stripe"></div>
  <div class="brand" style="left:34px; top:30px;">
    <span class="brand__dot" style="width:50px;height:50px;"></span>
    <span class="brand__name" style="font-size:15px;">Havelstädter<br>Fachschule<br>für Hautpflege</span>
  </div>
  <div class="header-rule" style="top:108px;"></div>
  <div class="photo photo--duo" role="img" aria-label="Foto: zwei lachende junge Frauen mit Gurkenscheiben vor den Augen" style="left:0; top:110px; width:440px; height:342px;"></div>
  <p class="slogan slogan--light" style="left:218px; top:132px; font-size:17px;">Siehst du deine Zukunft<br>&nbsp;&nbsp;noch nicht ganz klar?</p>
  <p class="info-phone" style="left:40px; top:412px; font-size:15px;">Infos unter 030/555 01 92</p>
  <div class="badge" style="left:336px; top:358px; width:84px; height:84px; font-size:12px;"><span>Staatl.<br>Förderung<br>möglich!</span></div>
  <div class="band" style="top:452px; height:168px; padding:22px 34px 0;">
    <p class="band__intro" style="font-size:11px;">Mit nur <strong>einer Ausbildung</strong> fit für <strong>drei Branchen:</strong></p>
    <p class="band__claim" style="font-size:20px; margin-top:6px;">Beauty, Health &amp; Wellness!</p>
    <p class="band__web" style="font-size:12px; margin-top:14px;">www.hautpflegeschule-havel.de</p>
  </div>
</section>

<section class="piece card card--front">
  <div class="top-stripe"></div>
  <div class="brand" style="left:30px; top:38px;">
    <span class="brand__dot" style="width:56px;height:56px;"></span>
    <span class="brand__name" style="font-size:16px;">Havelstädter<br>Fachschule<br>für Hautpflege</span>
  </div>
  <div class="header-rule" style="top:124px;"></div>
  <div class="photo photo--duo" role="img" aria-label="Foto: zwei lachende junge Frauen mit Gurkenscheiben vor den Augen" style="left:0; top:126px; width:330px; height:232px;"></div>
  <p class="slogan slogan--light" style="left:24px; top:292px; font-size:15px;">Siehst du deine Zukunft<br>&nbsp;noch nicht ganz klar?</p>
  <div class="band" style="top:358px; height:112px; padding:16px 30px 0;">
    <p class="band__intro" style="font-size:12px; line-height:1.3;">Mit nur <strong>einer Ausbildung</strong><br>fit für <strong>drei Branchen:</strong></p>
    <p class="band__claim" style="font-size:15px; margin-top:14px;">Beauty, Health &amp; Wellness!</p>
  </div>
  <div class="badge" style="left:232px; top:310px; width:80px; height:80px; font-size:11px;"><span>Staatl.<br>Förderung<br>möglich!</span></div>
</section>

<section class="piece card card--back">
  <div class="top-stripe"></div>
  <div class="back-copy" style="top:34px;">
    <p>Seit 50 Jahren erfolgreich, bieten wir<br>eine zweijährige anspruchsvolle und qualifizierte<br>Ausbildung zur Medizinischen Kosmetikerin an.</p>
    <p class="accent-pink">Nächster Ausbildungsbeginn: 1. Oktober!<br>Infos unter 030/555 01 92</p>
    <p>HFH GmbH, Nähe Lindenring</p>
    <p class="accent-green">Wir freuen uns auf DICH!</p>
  </div>
  <div class="photo photo--solo" role="img" aria-label="Foto: lachende junge Frau, die in eine Gurkenscheibe beißt" style="left:0; top:204px; width:170px; height:146px;"></div>
  <p class="slogan" style="left:160px; top:232px; font-size:17px; transform:rotate(10deg);">Meine Zukunft<br>&nbsp;beginnt JETZT!</p>
  <div class="band" style="top:350px; height:120px; padding:24px 0 0; text-align:center;">
    <p class="band__web" style="font-size:11px; opacity:.9;">Besuchen Sie uns auch im Web:</p>
    <p class="band__web" style="font-size:12px; margin-top:12px; line-height:1.4;">www.hautpflegeschule-havel.de<br>www.traumberuf-hautpflege.de</p>
  </div>
  <div class="badge" style="left:226px; top:300px; width:78px; height:78px; font-size:11px;"><span>Staatl.<br>Förderung<br>möglich!</span></div>
</section>

</body>
</html>
```